Copper lark buildworks

Copper lark buildworks is a small construction company.
Who is a licenced builder, Carpenter, joiner,
working on heritage ,new build, speacial projects and sometimes furniture

Industry/Entity Type

Construction

```html
<!DOCTYPE html>
<html lang="en">
<head>
<meta charset="utf-8">
<title>Copper lark buildworks – Business Card</title>
<link rel="stylesheet" href="https://fonts.googleapis.com/css2?family=Roboto:wght@400;700&display=swap">
<style>
  :root {
    --backdrop: #9a9a9a;
    --card: #1e1e1e;
    --card-edge: #262626;
    --brand-green: #3f9e45;
    --phone-white: #f2f2f2;
  }
  * { margin: 0; padding: 0; box-sizing: border-box; }
  html, body {
    width: 1200px;
    height: 900px;
    overflow: hidden;
  }
  body {
    background: var(--backdrop);
    display: flex;
    align-items: center;
    justify-content: center;
    font-family: "Roboto", Arial, sans-serif;
  }
  .business-card {
    width: 840px;
    height: 480px;
    border-radius: 30px;
    background: linear-gradient(160deg, var(--card-edge), var(--card) 60%);
    display: flex;
    flex-direction: column;
    align-items: center;
    padding-top: 150px;
    text-align: center;
  }
  .company-name {
    color: var(--brand-green);
    font-weight: 700;
    font-size: 48px;
    line-height: 1.1;
  }
  .person-name {
    color: var(--brand-green);
    font-weight: 700;
    font-size: 36px;
    margin-top: 14px;
    line-height: 1.1;
  }
  .phone-number {
    color: var(--phone-white);
    font-weight: 400;
    font-size: 27px;
    margin-top: 8px;
    letter-spacing: 0.5px;
  }
</style>
</head>
<body>
  <section class="business-card">
    <h1 class="company-name">Copper lark buildworks</h1>
    <p class="person-name">Marcus Hale</p>
    <p class="phone-number">0491570156</p>
  </section>
</body>
</html>
```